Neue Etiketten für die Weinflaschen der Lorenz Stiftung
Zielgruppe
Lorenz Stiftung ist eine soziale Institution. Hier leben und arbeiten rund 170 Menschen mit einer kognitiven Beeinträchtigung. Die Zielgruppe der Weine sind Privatpersonen aus dem Umfeld. Weitere Details siehe Briefing.
Aufgabenstellung
siehe Briefing, CD-Manual, etc.

```html
<!DOCTYPE html>
<html lang="de">
<head>
<meta charset="utf-8">
<title>Lorenz Stiftung – Rotwein Etikett</title>
<link rel="stylesheet" href="https://fonts.googleapis.com/css2?family=Merriweather:wght@700&display=swap">
<style>
  :root {
    --page-bg: #ffffff;
    --wine-red: #8f1418;
    --ink: #1c1c1c;
    --band: #1a1a1a;
    --band-text: #f2f2f2;
    --paper-light: #f4eeee;
    --paper-pink: #d9bfc1;
    --paper-rose: #c9a6aa;
  }
  * { margin: 0; padding: 0; box-sizing: border-box; }
  html, body {
    width: 1200px;
    height: 790px;
    overflow: hidden;
    background: var(--page-bg);
  }
  .canvas {
    width: 1200px;
    height: 790px;
    display: flex;
    align-items: center;
    justify-content: center;
  }
  .label {
    position: relative;
    width: 420px;
    height: 704px;
    display: flex;
    flex-direction: column;
    font-family: "Merriweather", Georgia, serif;
    font-weight: 700;
  }
  .label-artwork {
    position: relative;
    height: 614px;
    background:
      radial-gradient(ellipse 60% 40% at 30% 20%, var(--paper-light) 0%, transparent 70%),
      radial-gradient(ellipse 50% 35% at 75% 70%, var(--paper-rose) 0%, transparent 75%),
      radial-gradient(ellipse 55% 40% at 25% 80%, var(--paper-light) 0%, transparent 70%),
      linear-gradient(160deg, var(--paper-pink) 0%, var(--paper-light) 45%, var(--paper-pink) 100%);
  }
  .coordinates {
    position: absolute;
    inset: 0;
    line-height: 1;
  }
  .coordinate {
    position: absolute;
    font-size: 42px;
    letter-spacing: -0.5px;
    white-space: nowrap;
  }
  .coordinate--lat { left: 70px; top: 226px; color: var(--wine-red); }
  .coordinate--lon { left: 97px; top: 264px; color: var(--ink); }
  .wine-type {
    position: absolute;
    left: 0;
    right: 0;
    top: 554px;
    text-align: center;
    font-size: 24px;
    line-height: 1;
    color: var(--wine-red);
  }
  .label-band {
    flex: 1;
    background: var(--band);
    display: flex;
    align-items: center;
    justify-content: center;
  }
  .brand-name {
    font-size: 20px;
    letter-spacing: 2px;
    color: var(--band-text);
  }
</style>
</head>
<body>
  <main class="canvas">
    <article class="label">
      <div class="label-artwork" role="img" aria-label="Reliefartige Landschaft aus Papierschichten in Rosé- und Weißtönen, wie Höhenlinien einer Karte">
        <div class="coordinates">
          <span class="coordinate coordinate--lat">46°31‘22“N</span>
          <span class="coordinate coordinate--lon">17°48‘36“E</span>
        </div>
        <p class="wine-type">Rotwein</p>
      </div>
      <footer class="label-band">
        <span class="brand-name">Lorenz Stiftung</span>
      </footer>
    </article>
  </main>
</body>
</html>
```